Tourism Marketing needing sleek, clear design for business card & proposal documents.

***Company background***
"Quiet Harbour" is a company specializing in tourism marketing and project management. We do international wholesale, event management as well as ongoing representation of tourism and hospitality companies.

***Target market***
We cater to tourism companies and hotel professionals.

***Task***
We would like to get a single sided business card designed (but will still consider two sided, we are open to any ideas you may have). The layout for this card should be modern and elegant. Currently we do not have a logo, but we would like our business name in a really simple typography for the business card (similar to Moonrise Palace's logo - www.moonrisepalace-example.com.au).We are after a design that is clear, strong enough to be recognised as Quiet Harbour that does not require any fancy design. Another option is a simple play on QH (Quiet Harbour) or simply have Quiet Harbour featured elsewhere on card more as a brand/logo.

Feel free to submit different fonts if you feel you have any other fonts/designs that may be suitable for this card other than sans serifs. Should this project be successful, we will be considering several other projects for business proposal templates and eventually a website design.

The information that needs to go on the card are as follows:

Marta Holloway
Director
Quiet Harbour
Tourism Marketing & Representation
87 Wendover Parade
Larkmoor, Victoria, 3990 Australia
T +61 498203617 E marta@quietharbour-example.com.au

***Look and feel***
We'd like the business card design to express the following:
Modern, sleek, elegant, simple, discreet, quality, subtle, professional, creative, innovation

In terms of typography, we like something really simple and blocky (similar font to Moonrise Palace's logo - www.moonrisepalace-example.com.au)

***Colour scheme***
Shades of grey and dark teal

***Note***
Although our main target market are professionals, we would like the business card design to be versatile enough to be used outside of the tourism industry and need to appeal to different markets.

I do not have existing logo. Was hoping for a design that may be clear, strong enough not to require one. Other option is a simple play on QH (Quiet Harbour) or simply have Quiet Harbour featured elsewhere on card more as a brand/logo.

Marta Holloway
Director
Quiet Harbour Pty Ltd 
87 Wendover Parade
T +61 498203617  E  marta@quietharbour-example.com.au

Thank you for designs so far. Many have used a mauve colour which matches our company profile. This is not necessary, as that is just a draft and will be completely redesigned, so dont  feel you need to incorporate the mauve.

My colour preferences are for a white or grey background, and I like fonts in dark teals, grey or other sophisticated but modern colours. feel free to submit different fonts if you you have other fonts you thing would be suitable for this card, along with sans serifs. Should this project be successful, we will be considering several others for business proposal templates and eventually website. 

Target Market(s)

International Hospitality Senior Executives, Directors of International Tourism Companies, Directors of Tourism Bodies Internationally, local Tourism

Industry/Entity Type

Hospitality

Requirements
Should not have
• must not have bright garish colour, swirly patterns or anything that dates too much.

```html
<!DOCTYPE html>
<html lang="en">
<head>
<meta charset="utf-8">
<title>Quiet Harbour — Business Card</title>
<link rel="stylesheet" href="https://fonts.googleapis.com/css2?family=Barlow:wght@400;500;600&display=swap">
<style>
  :root {
    --backdrop: #cfcdca;
    --card: #f3f3f5;
    --teal-deep: #0f4d59;
    --teal-text: #1d5863;
  }
  * { margin: 0; padding: 0; box-sizing: border-box; }
  html, body {
    width: 1200px;
    height: 1000px;
    overflow: hidden;
    background: var(--backdrop);
    font-family: "Barlow", sans-serif;
  }
  .canvas {
    position: relative;
    width: 1200px;
    height: 1000px;
  }
  .card {
    position: absolute;
    width: 440px;
    height: 759px;
    background: var(--card);
    box-shadow: 0 6px 18px rgba(0, 0, 0, 0.18);
  }
  .card--front { left: 104px; top: 134px; }
  .card--back  { left: 652px; top: 132px; }

  .brand {
    position: absolute;
    left: 50px;
    top: 344px;
    color: var(--teal-deep);
  }
  .brand__name {
    font-weight: 600;
    font-size: 44px;
    line-height: 44px;
    letter-spacing: 1.7px;
    text-transform: uppercase;
    white-space: nowrap;
  }
  .brand__tagline {
    margin-top: 0;
    font-weight: 400;
    font-size: 20.5px;
    line-height: 24px;
    letter-spacing: 0.5px;
    white-space: nowrap;
  }

  .person {
    position: absolute;
    left: 45px;
    top: 208px;
    color: var(--teal-deep);
  }
  .person__name {
    font-size: 28px;
    line-height: 34px;
    letter-spacing: 1.5px;
  }
  .person__role {
    font-weight: 500;
    font-size: 19.5px;
    line-height: 22px;
    letter-spacing: 0.4px;
  }

  .details {
    position: absolute;
    left: 46px;
    top: 527px;
    color: var(--teal-text);
    font-size: 19.5px;
    line-height: 24px;
    letter-spacing: 0.9px;
    white-space: nowrap;
  }
  .details__group + .details__group { margin-top: 24px; }
  .details__label { display: inline-block; width: 22px; }
  .details__email { letter-spacing: 0.6px; }
</style>
</head>
<body>
  <main class="canvas">
    <section class="card card--front" aria-label="Card front">
      <div class="brand">
        <div class="brand__name">Quiet Harbour</div>
        <div class="brand__tagline">Tourism Marketing &amp; Representation</div>
      </div>
    </section>

    <section class="card card--back" aria-label="Card back">
      <div class="person">
        <div class="person__name">Marta Holloway</div>
        <div class="person__role">Director</div>
      </div>

      <div class="details">
        <div class="details__group">
          <div>Quiet Harbour Pty Ltd</div>
          <div>Tourism Marketing &amp; Representation</div>
        </div>
        <div class="details__group">
          <div>87 Wendover Parade</div>
          <div>Larkmoor, Victoria, 3990 Australia</div>
        </div>
        <div class="details__group">
          <div><span class="details__label">T</span>+61 498203617</div>
          <div class="details__email"><span class="details__label">E</span>marta@quietharbour-example.com.au</div>
        </div>
      </div>
    </section>
  </main>
</body>
</html>
```